Recruitment of Brindle Staffing for the UK market

I want a website for the UK market to attract businesses and companies to come to us for Philipine labour. We want an information site that gives all information on what we do and how we can recruit Philippine labour.
This is a recruitment site for companies to contact us with their requirements for skilled workers coming from the Philipines over to the UK to work.

Target Market(s)

Uk Companies and businesses who want Philipine skilled workers

Industry/Entity Type

REcruitment

Coding

Coded - Design and coding required

Number of Pages Required

5+ page

Font styles to use
Sans Serif

Colors
0054AA
0677BA
7BADD7
CADEEF
E8F1F8
0094D4
00A9DD
6FCCEA
C7EBF8
E9F6FB
EE7325
F08F49
F5BC92
FAE3D3
FDF4ED
EB3D1F
EC4F4E
F09395
F8D3D4
FCEDEE

Requirements
Must have
• Look professional and corperate with drop down menus for Home ,about, services,articles. training , contact us
Nice to have
• Look at Tovel recruitment- https://tovelrecruitment.example.co.uk/. This is my current site - https://www.brindlestaffing.example.com/
Should not have
• Cartoons or silly pictures , needs to be corperate looking

```html
<!DOCTYPE html>
<html lang="en">
<head>
<meta charset="utf-8">
<title>Brindle Staffing</title>
<link href="https://fonts.googleapis.com/css2?family=Poppins:wght@400;500;600;700&family=Lato:wght@400;700&display=swap" rel="stylesheet">
<style>
:root{
  --orange:#EE7325;
  --orange-light:#F08F49;
  --orange-pale:#FAE3D3;
  --orange-mist:#FDF4ED;
  --blue-mist:#EEF5FC;
  --ink:#1d1d1d;
  --text:#444;
  --muted:#666;
  --brand:#9b1f1f;
  --white:#fff;
  --form-bg:#F5F3EF;
}
*{box-sizing:border-box;margin:0;padding:0}
html,body{width:1200px;height:3887px;overflow:hidden}
body{position:relative;background:var(--white);font-family:'Poppins',sans-serif;color:var(--text)}
.abs{position:absolute}
.brand{font-family:'Poppins',sans-serif;font-weight:700;color:var(--brand);font-size:26px;letter-spacing:.3px}
/* header */
.site-header{left:0;top:0;width:1200px;height:81px;background:var(--white);z-index:2}
.site-header .brand{left:113px;top:22px}
.main-nav a{position:absolute;top:30px;font-size:15px;color:var(--ink);text-decoration:none}
.btn-login{left:1014px;top:23px;width:74px;height:33px;background:var(--orange);color:var(--white);font-size:13px;display:flex;align-items:center;justify-content:center;border-radius:3px}
/* hero */
.hero-photo{left:113px;top:81px;width:1087px;height:643px;background:linear-gradient(110deg,#f4f4f4 0%,#e6e6e6 35%,#9a9c9f 70%,#5b5e63 100%)}
.hero-fade{left:0;top:81px;width:700px;height:643px;background:linear-gradient(90deg,#fff 40%,rgba(255,255,255,0))}
.hero-title{left:113px;top:378px;font-size:45px;line-height:52px;font-weight:700;color:var(--orange)}
.hero-sub{left:113px;top:494px;font-size:21px;line-height:31px;color:#333;width:460px}
.btn{display:flex;align-items:center;justify-content:center;font-weight:600;text-transform:uppercase;border-radius:2px}
.btn-solid{background:var(--orange);color:var(--white)}
.btn-outline{border:1.5px solid var(--orange);color:var(--orange);background:var(--white)}
.hero-btn{left:113px;top:569px;width:118px;height:32px;font-size:13px;font-weight:500}
.dots span{position:absolute;top:623px;width:16px;height:16px;border-radius:50%;border:2px solid var(--orange-light)}
.dots span.on{background:var(--orange);border-color:var(--orange)}
/* services */
.section-title{width:1200px;left:0;text-align:center;font-weight:700;color:var(--ink);font-size:30px}
.service-card{top:880px;width:225px}
.service-img{height:169px;border-radius:8px}
.service-card h3{margin-top:20px;text-align:center;color:var(--orange);font-size:20px;font-weight:600}
.service-card p{margin-top:14px;text-align:center;font-size:15px;line-height:26.5px;color:var(--text)}
.service-card .btn{margin:18px auto 0;width:142px;height:38px;font-size:13px}
.arrow{top:1040px}
/* about */
.about-band{left:0;top:1334px;width:1200px;height:587px;background:var(--blue-mist)}
.about-title{left:97px;top:1484px;font-size:31px;line-height:41px;font-weight:700;color:var(--ink);text-transform:uppercase}
.about-text{left:97px;top:1580px;width:397px;font-size:15px;line-height:24px;text-align:justify;color:#222}
.about-btn{left:97px;top:1740px;width:116px;height:31px;font-size:11px}
.photo{border-radius:0}
/* working together */
.work-band{left:0;top:1921px;width:1200px;height:619px;background:linear-gradient(180deg,#E2692A 0%,#EE7325 55%,#E8702A 100%)}
.work-title{top:1998px;color:var(--white)}
.work-card{top:2078px;width:317px;height:367px;background:var(--white);text-align:center}
.work-icon{margin:30px auto 0;width:96px;height:96px;border-radius:50%;background:var(--orange-pale);display:flex;align-items:center;justify-content:center}
.work-card h3{margin-top:14px;color:var(--orange);font-size:22px;font-weight:600}
.work-card p{margin:10px auto 0;width:270px;font-size:15.5px;line-height:24.5px;color:var(--muted);height:100px}
.work-card .btn{margin:0 auto;width:140px;height:38px;font-size:13px}
/* blog */
.blog-title{left:112px;top:2615px;font-size:31px;line-height:45px;font-weight:700;color:var(--ink)}
.blog-intro{left:112px;top:2714px;width:400px;font-family:'Lato',sans-serif;font-size:15px;line-height:24px;color:#222}
.view-more{left:112px;top:2797px;font-family:'Lato',sans-serif;font-size:16px;color:var(--orange);display:flex;align-items:center;gap:10px}
.post{left:601px;width:487px}
.post h3{font-size:19px;font-weight:600;color:var(--orange)}
.post p{margin-top:10px;font-family:'Lato',sans-serif;font-size:14.5px;line-height:22px;text-align:justify;color:#222}
.post svg{margin-top:8px}
/* contact */
.map{left:0;top:3044px;width:600px;height:457px;background:linear-gradient(135deg,#8fb0e8 0%,#9dbbeb 40%,#b9d3a8 60%,#8fb0e8 100%)}
.form-area{left:600px;top:3044px;width:600px;height:457px;background:var(--form-bg)}
.field{left:644px;width:491px;height:55px;background:var(--white);border:1px solid #ececec;padding:16px 13px;font-size:14.5px;color:#777}
.send-btn{left:644px;top:3404px;width:139px;height:37px;font-size:13px}
/* footer */
.footer-brand{left:150px;top:3585px;font-size:28px}
.footer-text{left:142px;top:3648px;font-size:15.5px;line-height:26px;color:#222}
.social{top:3723px;width:34px;height:34px;border-radius:50%;border:1.5px solid var(--orange)}
.social.on{background:var(--orange)}
.footer-col h4{font-size:20px;font-weight:600;color:var(--ink)}
.footer-col ul{list-style:none;margin-top:18px}
.footer-col li{font-family:'Lato',sans-serif;font-size:15px;line-height:27.5px;color:#222}
.contact-line{display:flex;gap:6px;align-items:flex-start;font-family:'Lato',sans-serif;font-size:15px;line-height:27.5px;color:#222}
.copyright{left:0;width:1200px;top:3831px;text-align:center;font-size:15px;color:#222}
.copyright b{color:var(--orange);font-weight:600}
</style>
</head>
<body>

<header class="site-header abs">
  <div class="brand abs">Brindle Staffing</div>
  <nav class="main-nav">
    <a style="left:422px">Home</a>
    <a style="left:511px">About</a>
    <a style="left:601px">Services</a>
    <a style="left:701px">Articles</a>
    <a style="left:798px">Training</a>
    <a style="left:897px">Contact Us</a>
  </nav>
  <div class="btn-login abs">LOG IN</div>
</header>

<section class="hero">
  <div class="hero-photo abs" role="img" aria-label="Row of white chairs with a single orange chair standing out"></div>
  <div class="hero-fade abs"></div>
  <h1 class="hero-title abs">Welcome To<br>Brindle Staffing</h1>
  <p class="hero-sub abs">Recruiting and placing skilled Philippine workers into UK companies</p>
  <div class="btn btn-solid hero-btn abs">Get Started</div>
  <div class="dots"><span class="on" style="left:111px"></span><span style="left:138px"></span><span style="left:165px"></span><span style="left:193px"></span></div>
</section>

<section class="services">
  <h2 class="section-title abs" style="top:790px">OUR SERVICES</h2>
  <svg class="arrow abs" style="left:44px" width="20" height="34" viewBox="0 0 20 34"><path d="M16 3 3 17l13 14" fill="none" stroke="#888" stroke-width="3"/></svg>
  <svg class="arrow abs" style="left:1134px" width="20" height="34" viewBox="0 0 20 34"><path d="M4 3l13 14L4 31" fill="none" stroke="#888" stroke-width="3"/></svg>
  <article class="service-card abs" style="left:110px">
    <div class="service-img" style="background:linear-gradient(180deg,#9fc3e6,#c9a77a)" role="img" aria-label="Civil engineers on a building site with a crane"></div>
    <h3>Civil Engineer</h3>
    <p>Lorem ipsum dolor sit amet, consectetur adipiscing elit, sed do eiusmod tempor</p>
    <div class="btn btn-outline">Apply Now</div>
  </article>
  <article class="service-card abs" style="left:361px">
    <div class="service-img" style="background:linear-gradient(180deg,#d9c7a6,#b58d5c)" role="img" aria-label="Highways engineer with tablet beside a road"></div>
    <h3>Highways Engineer</h3>
    <p>Lorem ipsum dolor sit amet, consectetur adipiscing elit, sed do eiusmod tempor</p>
    <div class="btn btn-outline">Apply Now</div>
  </article>
  <article class="service-card abs" style="left:611px">
    <div class="service-img" style="background:linear-gradient(180deg,#a9c6e3,#7e8fa3)" role="img" aria-label="Site engineers reviewing plans on a construction site"></div>
    <h3>Site Engineer</h3>
    <p>Lorem ipsum dolor sit amet, consectetur adipiscing elit, sed do eiusmod tempor</p>
    <div class="btn btn-outline">Apply Now</div>
  </article>
  <article class="service-card abs" style="left:862px">
    <div class="service-img" style="background:linear-gradient(180deg,#8a7260,#5c4a3c)" role="img" aria-label="Anthropologist excavating soil at a dig site"></div>
    <h3>Anthropologist</h3>
    <p>Lorem ipsum dolor sit amet, consectetur adipiscing elit, sed do eiusmod tempor</p>
    <div class="btn btn-outline">Apply Now</div>
  </article>
</section>

<section class="about">
  <div class="about-band abs"></div>
  <h2 class="about-title abs">What the business is<br>about</h2>
  <p class="about-text abs">We source skilled workers directly from the Philippines to work in the UK. With offices , training locations and specialist recruiters we can find the highest quality individuals to add value and resources to any UK buisness. We delivery quality based on vast experience over a number of years.</p>
  <div class="btn btn-solid about-btn abs">Read More</div>
  <div class="photo abs" style="left:566px;top:1429px;width:344px;height:236px;background:linear-gradient(180deg,#8fb5d3,#5f8fb6)" role="img" aria-label="Group of smiling workers in blue uniforms"></div>
  <div class="photo abs" style="left:566px;top:1671px;width:169px;height:155px;background:linear-gradient(180deg,#c9c2b6,#8e8578)" role="img" aria-label="Workers in hard hats reviewing a clipboard"></div>
  <div class="photo abs" style="left:740px;top:1671px;width:170px;height:155px;background:linear-gradient(180deg,#d8cdb8,#a09a92)" role="img" aria-label="Team of workers in hard hats and office wear"></div>
  <div class="photo abs" style="left:915px;top:1429px;width:285px;height:397px;background:linear-gradient(135deg,#e7edf2,#b8c3cd 60%,#2f3a4a)" role="img" aria-label="Businessman shaking hands across a desk"></div>
</section>

<section class="working">
  <div class="work-band abs" role="img" aria-label="Orange-tinted background of an office meeting"></div>
  <h2 class="section-title work-title abs">WORKING TOGETHER</h2>
  <article class="work-card abs" style="left:110px">
    <div class="work-icon"><svg width="54" height="46" viewBox="0 0 54 46"><rect x="17" y="2" width="20" height="10" rx="3" fill="none" stroke="#EE7325" stroke-width="4"/><rect x="2" y="10" width="50" height="34" rx="5" fill="#EE7325"/><rect x="22" y="22" width="10" height="7" rx="1" fill="#fff"/></svg></div>
    <h3>What We Do</h3>
    <p>Our company has been estabilished in the Philippines for over 20 years. We have mainly been recruiting philippine</p>
    <div class="btn btn-solid">View Openings</div>
  </article>
  <article class="work-card abs" style="left:442px">
    <div class="work-icon"><svg width="56" height="46" viewBox="0 0 56 46"><circle cx="28" cy="10" r="6" fill="#EE7325"/><circle cx="14" cy="14" r="5" fill="#EE7325"/><circle cx="42" cy="14" r="5" fill="#EE7325"/><path d="M18 30a10 10 0 0 1 20 0z" fill="#EE7325"/><path d="M6 28c0 10 8 14 16 16M50 28c0 10-8 14-16 16" fill="none" stroke="#EE7325" stroke-width="4" stroke-linecap="round"/></svg></div>
    <h3>How We Help</h3>
    <p>We work with companies to find skilled workers that meet the UK requirements for Visas and work permits.</p>
    <div class="btn btn-solid">View Openings</div>
  </article>
  <article class="work-card abs" style="left:773px">
    <div class="work-icon"><svg width="50" height="50" viewBox="0 0 50 50"><path d="M44 6C30 6 20 14 16 26l8 8c12-4 20-14 20-28z" fill="#EE7325"/><circle cx="32" cy="18" r="4" fill="#fff"/><path d="M16 26l-8 2 6-10 8-1zM24 34l-2 8 10-6 1-8z" fill="#EE7325"/><path d="M12 38l-6 6" stroke="#EE7325" stroke-width="4" stroke-linecap="round"/></svg></div>
    <h3>Where To start</h3>
    <p>We need to know what your issues are and how we can understand the personnal you require , over what time frame</p>
    <div class="btn btn-solid">View Openings</div>
  </article>
</section>

<section class="blog">
  <h2 class="blog-title abs">RECENT BLOG<br>ARTICLES</h2>
  <p class="blog-intro abs">Lorem ipsum dolor sit amet, consectetur adipiscing elit, sed do eiusmod tempor incididunt ut labore et dolore magna aliqua.</p>
  <div class="view-more abs">View More <svg width="36" height="24" viewBox="0 0 36 24"><circle cx="24" cy="12" r="10" fill="none" stroke="#EE7325" stroke-width="2"/><path d="M2 12h24M20 6l6 6-6 6" fill="none" stroke="#EE7325" stroke-width="2.4"/></svg></div>
  <article class="post abs" style="top:2618px">
    <h3>UK Skilled Workers List</h3>
    <p>The UK government since brexit have developed a new system based on points (similar to Australia) when recruiting from outside of the UK. Previuosly EU citizens could work in the UK without any extensive documentation or clarification of skills. .</p>
    <svg width="28" height="22" viewBox="0 0 28 22"><circle cx="16" cy="11" r="9" fill="none" stroke="#EE7325" stroke-width="2"/><path d="M1 11h18M14 6l5 5-5 5" fill="none" stroke="#EE7325" stroke-width="2.2"/></svg>
  </article>
  <article class="post abs" style="top:2802px">
    <h3>Sponsor Licence</h3>
    <p>If you have areas of your business that meet the entry requirements of skilled labour your next step is to gain a sponsor licence for your business. There are different types of licences depending on the size of the business.</p>
    <svg width="28" height="22" viewBox="0 0 28 22"><circle cx="16" cy="11" r="9" fill="none" stroke="#EE7325" stroke-width="2"/><path d="M1 11h18M14 6l5 5-5 5" fill="none" stroke="#EE7325" stroke-width="2.2"/></svg>
  </article>
</section>

<section class="contact">
  <div class="map abs" role="img" aria-label="Map of the Philippines with office location markers"></div>
  <div class="form-area abs"></div>
  <div class="field abs" style="top:3104px">Name</div>
  <div class="field abs" style="top:3178px">Phone</div>
  <div class="field abs" style="top:3252px">Email</div>
  <div class="field abs" style="top:3326px">Message</div>
  <div class="btn btn-solid send-btn abs">Send Message</div>
</section>

<footer class="site-footer">
  <div class="brand footer-brand abs">Brindle Staffing</div>
  <p class="footer-text abs">We recruit the finest talent available<br>with our dedicated 200 strong team</p>
  <span class="social on abs" style="left:147px"></span>
  <span class="social abs" style="left:199px;border:none"><svg width="34" height="34"><circle cx="17" cy="17" r="4" fill="#EE7325"/></svg></span>
  <span class="social abs" style="left:250px;border:none"><svg width="34" height="34"><circle cx="17" cy="17" r="4" fill="#EE7325"/></svg></span>
  <span class="social abs" style="left:301px;border:none"><svg width="34" height="34"><circle cx="17" cy="17" r="4" fill="#EE7325"/></svg></span>
  <div class="footer-col abs" style="left:566px;top:3570px">
    <h4>Quick Links</h4>
    <ul><li>Home</li><li>About</li><li>Services</li><li>Articles</li><li>Training</li><li>Contact Us</li></ul>
  </div>
  <div class="footer-col abs" style="left:780px;top:3570px;width:320px">
    <h4>Contact Us</h4>
    <div style="margin-top:18px">
      <div class="contact-line"><svg width="10" height="14" viewBox="0 0 10 14" style="margin-top:7px"><path d="M5 0a5 5 0 0 1 5 5c0 4-5 9-5 9S0 9 0 5a5 5 0 0 1 5-5z" fill="#EE7325"/><circle cx="5" cy="5" r="2" fill="#fff"/></svg><span>Elmstead Gardens, Hornbury Hornbury<br>HB12 4 United Kingdom</span></div>
      <div class="contact-line" style="margin-top:8px"><svg width="12" height="12" viewBox="0 0 12 12" style="margin-top:8px"><path d="M2 0l3 3-1.5 2a7 7 0 0 0 3.5 3.5L9 7l3 3-2 2C5 12 0 7 0 2z" fill="#EE7325"/></svg><span>+44 1632 960 000</span></div>
      <div class="contact-line" style="margin-top:6px"><svg width="14" height="11" viewBox="0 0 14 11" style="margin-top:9px"><rect width="14" height="11" rx="1" fill="#EE7325"/><path d="M1 1l6 5 6-5" fill="none" stroke="#fff" stroke-width="1.3"/></svg><span>sales@brindlestaffing.example.com</span></div>
    </div>
  </div>
  <p class="copyright abs">Copyright © 2023 <b>Brindle Staffing</b> &nbsp;|&nbsp; All rights reserved.</p>
</footer>

</body>
</html>
```